Salt Water Delivery Company Business Card Design

We are a company that delivers natural saltwater (from the ocean) to aquarium companies, restaurants and home marine tanks. I would like a new business card to suit.

Must include Name, company name, abn, contact number and website as well as logo (see attached).

Looking for a design that stands out, has a clean but unique appearance.

Double and single sided entries welcome

Industry/Entity Type

Business

Requirements
Must have
• Logo

```html
<!DOCTYPE html>
<html lang="en">
<head>
<meta charset="utf-8">
<title>Tidewell Business Card</title>
<link href="https://fonts.googleapis.com/css2?family=Questrial&display=swap" rel="stylesheet">
<style>
  :root {
    --stage: #000000;
    --ocean-light: #2fb4f0;
    --ocean-mid: #1456e0;
    --ocean-deep: #0a1a8c;
    --ocean-night: #050a3a;
    --paper: #ffffff;
    --ink: #1c1c8c;
    --mist: rgba(225, 235, 255, 0.72);
  }
  * { margin: 0; padding: 0; box-sizing: border-box; }
  html, body {
    width: 940px;
    height: 1200px;
    overflow: hidden;
    background: var(--stage);
    font-family: "Questrial", sans-serif;
  }
  .card {
    position: absolute;
    left: 61px;
    width: 806px;
    height: 496px;
    overflow: hidden;
  }
  .card-front {
    top: 64px;
    background:
      radial-gradient(ellipse at 30% 10%, rgba(90, 200, 255, 0.55), transparent 55%),
      linear-gradient(170deg, var(--ocean-light) 0%, var(--ocean-mid) 40%, var(--ocean-deep) 75%, var(--ocean-night) 100%);
  }
  .card-back { top: 630px; background: var(--paper); }

  .brand-name {
    position: absolute;
    left: 0;
    right: 0;
    text-align: center;
    color: var(--paper);
    font-weight: 400;
    letter-spacing: -1px;
  }
  .card-front .brand-name { top: 160px; font-size: 128px; }

  .website {
    position: absolute;
    left: 0;
    right: 0;
    text-align: center;
    color: var(--mist);
    font-size: 29px;
    letter-spacing: 0.3px;
  }
  .card-front .website { top: 452px; }

  .back-header {
    position: absolute;
    top: 0; left: 0; right: 0;
    height: 144px;
    background:
      radial-gradient(ellipse at 40% 0%, rgba(110, 215, 255, 0.7), transparent 60%),
      linear-gradient(180deg, var(--ocean-light) 0%, var(--ocean-mid) 100%);
  }
  .back-header .brand-name { top: 40px; font-size: 56px; }

  .back-footer {
    position: absolute;
    top: 365px; left: 0; right: 0; bottom: 0;
    background:
      radial-gradient(ellipse at 50% 100%, rgba(40, 90, 255, 0.6), transparent 65%),
      linear-gradient(180deg, var(--ocean-deep) 0%, var(--ocean-mid) 55%, var(--ocean-night) 100%);
  }
  .back-footer .website { top: 58px; }

  .holder-name {
    position: absolute;
    left: 49px;
    top: 238px;
    font-size: 40px;
    color: var(--ink);
    border-bottom: 2px solid var(--ink);
    line-height: 1.1;
  }
  .contact-list { position: absolute; left: 0; top: 0; }
  .contact-line {
    position: absolute;
    display: flex;
    align-items: center;
    gap: 12px;
    font-size: 25px;
    color: var(--ink);
    white-space: nowrap;
  }
  .contact-phone { left: 448px; top: 196px; }
  .contact-email { left: 448px; top: 232px; }
  .contact-abn { left: 416px; top: 270px; }
  .contact-icon {
    width: 27px;
    height: 27px;
    flex: none;
  }
</style>
</head>
<body>
  <section class="card card-front">
    <h1 class="brand-name">Tidewell</h1>
    <p class="website">www.tidewellsupply.com.au</p>
  </section>

  <section class="card card-back">
    <header class="back-header">
      <h2 class="brand-name">Tidewell</h2>
    </header>

    <p class="holder-name">Your Name</p>

    <div class="contact-list">
      <p class="contact-line contact-phone">
        <svg class="contact-icon" viewBox="0 0 28 28" aria-hidden="true">
          <rect width="28" height="28" rx="5" fill="#1c1c8c"/>
          <path d="M9 7c-1.5 1-2 3 0 7s5 6.5 7.5 7c1.5.3 2.5-.5 3.3-1.6l-2.6-2.4-2 1.2c-1.3-.6-3.6-3-4.2-4.4l1.2-2L9.7 6.6z" fill="#ffffff"/>
        </svg>
        <span>123 456 78</span>
      </p>
      <p class="contact-line contact-email">
        <svg class="contact-icon" viewBox="0 0 28 28" aria-hidden="true">
          <rect width="28" height="28" rx="5" fill="#1c1c8c"/>
          <rect x="6" y="8.5" width="16" height="11" rx="1" fill="#ffffff"/>
          <path d="M6.5 9l7.5 6 7.5-6" fill="none" stroke="#1c1c8c" stroke-width="1.4"/>
        </svg>
        <span>your-email@tidewell.au</span>
      </p>
      <p class="contact-line contact-abn">ABN 123-456-789</p>
    </div>

    <footer class="back-footer">
      <p class="website">www.tidewellsupply.com.au</p>
    </footer>
  </section>
</body>
</html>
```